Real Estate Website

I have a very old website that was built almost 20 years ago. We are rebuilding it and need a fresh new design for it please.
The existing website is https://northpeakhomes.example

This is for a real estate company that is selling real estate in Hokkaido, Japan (known for it's skiing and snow tourism) and is all in english as it targets westerners looking to buy holiday homes or investment properties.
Updates

Hi everyone.

Sorry this has taken so long to get back to you. My client has taken a long time to get back to me after the Christmas break.

Unfortunately they did not want to go ahead with any of the designs submitted as they said they look too much like business sales websites instead of residential and commercial sales. An example of what they lik is https://www.vantoproperty.example/
They don't want it to look at all like their business sales website (https://www.lorvanebizsales.example/) and have said:

• keep Lo RVANE GROUP logo and color scheme the same
• Give freedom to the designers, on how what to execute what the company does.
-Commercial/Industrial
-Residential

Make them separate as there’s a different audience of clients for commercial & residential are very different.

I will provide some content and headings which you have the freedom to play around and coordinate. What I provide below are only suggestions, please feel free to be use your ideas and be innovative.

Residential listings - would like the listing to shows Features on details page.
Commercial listings – must display “building area” on the front page
HEADINGS ON TOP OF PAGE -TABS:
HOME - This MUST show on the tab
COMMERCIAL/INDUSTRIAL - This MUST show on the tab
RESIDENTIAL - This MUST show on the tab
BUSINESS SALES (this to link straight to my LO RVANE BUSINESS SALES & VUALUATIONS website - This MUST show on the tab
ABOUT US
BLOGS/videos- I want my team to be able to load all the videos, eg when they do videos for auctions, developments etc -– optional, if not enough space, show it on the bottom of the website ( you could also add under ABOUT US tab)
CONTACT US

Maybe show this on the home screen heading:
Specialists in Commercial/ Industrial Property,
Trusted in Residential Property

Theme:
“Maximising returns, protecting investments, expert property advisory”
Work With Us

The Information below is not in any particle order:

Book an Appraisal
Discover the Real Value of Your Property
At Lorvane Group, we don’t just provide standard appraisals — we deliver strategic, insight-driven reports that uncover the true drivers of your property’s worth. Whether it’s commercial, industrial, or residential, our expertise ensures you see the full picture.
From market trends and rental potential to investment performance and future growth opportunities, our tailored reports give you clarity, confidence, and actionable insights.
Book a confidential consultation today and gain the expert guidance you need to maximise returns and make smarter property decisions.

What We Do
What We Do – Property Management, Sales & Leasing
At Lorvane Group, we specialise in guiding property owners, investors, and landlords through the complexities of managing, selling, leasing, and valuing assets. Our mission is clear: to deliver clarity, confidence, and measurable results at every stage of your property journey.
We go beyond standardised reports. Our strategic, insight-driven valuations and management solutions uncover the true drivers of your property’s performance. From tailored marketing campaigns and compelling listings to confidential negotiations and introductions, we ensure your asset attracts the right tenants, buyers, or investors.
When the future of your investment is on the line, you need more than a property manager or agent — you need a partner who delivers certainty, strategy, and results. At Lorvane Group, we don’t just manage, lease, or sell properties; we maximise value, income, and long-term growth.
Contact us today for a confidential consultation and discover how Lorvane Group can help you achieve the strongest outcomes for your property portfolio.

Who We Are
At Lorvane Group, we are recognised as a trusted authority in commercial and residential property management, sales, and leasing. Property owners, investors, and developers turn to us for our proven expertise, discretion, and consistent results.
Our mission is to set the standard for excellence in property services. Guided by innovation, integrity, and strategic execution, we deliver outcomes that protect assets, maximise returns, and create enduring value for our clients.
Whether your goal is to manage your investment, increase rental income, lease to the right tenants, or achieve a successful sale, we provide clarity, confidence, and tailored solutions at every stage of the journey.
Let’s begin the conversation today — and explore how Lorvane Group can help you achieve the strongest results for your property portfolio.

Commercial & Industrial Property Management & Leasing

At Lorvane Group, we are recognised as a leading authority in the management and leasing of premium commercial and industrial assets. Trusted by investors, landlords, and developers, our portfolio spans medical centres, healthcare facilities, allied health clinics, global franchise brands such as BQJ and The Waffle Pantry Co, high‑end retail outlets, and large‑scale industrial and manufacturing properties.
We deliver strategic, results‑driven property solutions that combine market intelligence, operational excellence, and meticulous attention to detail. Our approach is designed to maximise returns, minimise vacancies, and safeguard long‑term asset performance.

Our Services
• Strategic Marketing & Leasing – Positioning your property to attract premium tenants through targeted, multi‑channel campaigns.
• Tenant & Lease Administration – Precision management of agreements, renewals, compliance, and documentation.
• Revenue Optimisation – Proactive rent collection, vacancy minimisation, and lease structuring to elevate asset value.
• Maintenance & Property Upkeep – Access to vetted, high‑quality trades for repairs and preventative care, ensuring assets remain in peak condition.
• Regulatory Compliance & Essential Services – Full oversight of statutory obligations and essential service measures, protecting both compliance and reputation.
Why Choose us
• Sector Expertise – Deep knowledge across medical, healthcare, franchise, retail, and industrial sectors, enabling tailored strategies for each asset class.
• Proactive Asset Management – Beyond operations, we actively enhance value, mitigate risk, and secure the right tenants.
• Bespoke Solutions – Every property is unique. We craft customised management and leasing strategies aligned with your objectives and market conditions.
• Professional Excellence – Integrity, precision, and industry‑leading best practices deliver measurable results and peace of mind for discerning property owners.
With Lorvane Group, your commercial and industrial assets are managed with authority, insight, and excellence — ensuring performance that meets the expectations of high‑end investors and developers.

```html
<!DOCTYPE html>
<html lang="en">
<head>
<meta charset="utf-8">
<title>Northpeak Homes</title>
<link href="https://fonts.googleapis.com/css2?family=Cinzel:wght@500;700&family=Nunito+Sans:wght@400;600;700&family=Poppins:wght@400;500;600&display=swap" rel="stylesheet">
<style>
:root{
  --red:#c8282d;
  --red-dark:#a81e23;
  --ink:#222;
  --text:#444;
  --muted:#777;
  --nav-bg:#f5f2ee;
  --grey-bg:#eeeeee;
  --line:#e2e2e2;
  --black:#000;
  --white:#fff;
}
*{margin:0;padding:0;box-sizing:border-box}
html,body{width:1200px;height:4179px;overflow:hidden}
body{position:relative;font-family:"Nunito Sans",sans-serif;color:var(--text);background:var(--white)}
.abs{position:absolute}

/* top bar */
.topbar{top:0;left:0;width:1200px;height:42px;background:var(--red);color:#fff;font-size:15px;font-family:"Poppins",sans-serif}
.social{left:110px;top:14px;display:flex;gap:9px}
.social span{width:14px;height:14px;border-radius:50%;background:#fff;display:block}
.top-contact{right:110px;top:10px;display:flex;gap:34px;align-items:center}
.top-contact div{display:flex;gap:8px;align-items:center}

/* nav */
.nav{top:42px;left:0;width:1200px;height:88px;background:var(--nav-bg)}
.brand{left:112px;top:29px;display:flex;align-items:center;gap:9px;font-family:"Cinzel",serif;font-weight:700;font-size:18px;color:var(--red-dark);white-space:nowrap}
.brand i{width:24px;height:24px;background:var(--red);border-radius:50%;display:block}
.menu{left:366px;top:36px;display:flex;gap:17px;font-family:"Cinzel",serif;font-size:12.5px;font-weight:500;color:var(--ink);white-space:nowrap}
.menu .active{font-weight:700;position:relative}
.menu .active:before{content:"";position:absolute;left:50%;top:-10px;width:6px;height:6px;border-radius:50%;background:var(--red);margin-left:-3px}
.btn-contact{left:969px;top:24px;width:120px;height:38px;border-radius:19px;background:#222;color:#fff;font-family:"Cinzel",serif;font-weight:700;font-size:13px;display:flex;align-items:center;justify-content:center;white-space:nowrap}

/* hero */
.hero{top:130px;left:0;width:1200px;height:620px;overflow:hidden}
.hero-photo{position:absolute;inset:0;background:linear-gradient(160deg,#2a3446 0%,#3a3a3e 40%,#5a4a3c 70%,#2a2c33 100%)}
.hero-title{top:148px;left:0;width:1200px;text-align:center;font-family:"Cinzel",serif;font-weight:500;font-size:60px;color:#fff;letter-spacing:1px}
.hero-sub{top:220px;left:290px;width:620px;text-align:center;color:#fff;font-size:15.5px;line-height:25px}
.search{top:295px;left:287px;width:626px;height:42px;background:#fff;border-radius:21px;display:flex;align-items:center;font-size:13px;color:#555}
.search .f{height:100%;display:flex;align-items:center;padding-left:24px;border-right:1px solid #ddd}
.search .go{position:absolute;right:4px;top:4px;width:160px;height:34px;border-radius:17px;background:var(--red);color:#fff;font-family:"Cinzel",serif;font-weight:700;font-size:14px;display:flex;align-items:center;justify-content:center}
.audience{top:358px;left:0;width:1200px;display:flex;justify-content:center;gap:14px}
.audience span{height:32px;padding:0 20px;border-radius:16px;border:1.5px solid #fff;color:#fff;font-family:"Cinzel",serif;font-weight:700;font-size:12.5px;display:flex;align-items:center}
.audience .on{background:#fff;color:var(--red)}
.mouse{top:478px;left:588px}
.hero-wave{left:0;bottom:0}

/* section headings */
.h2{font-family:"Cinzel",serif;font-weight:700;color:var(--ink);text-align:center;font-size:34px;width:1200px;left:0}
.rule{height:3px;width:48px;background:var(--red)}

/* welcome */
.w-frame{left:98px;top:857px;width:284px;height:266px;border:2px solid var(--red);border-bottom:none;border-right:none}
.w-frame-red{left:98px;top:857px;width:148px;height:14px;background:var(--red)}
.w-frame-side{left:98px;top:857px;width:12px;height:240px;background:var(--red)}
.w-photo{left:109px;top:871px;width:444px;height:390px;background:linear-gradient(180deg,#3f6fb0 0%,#6d8fb8 35%,#c9d3df 55%,#5a78a8 75%,#2d4f86 100%)}
.badge{left:484px;top:1007px;width:118px;height:118px;border-radius:50%;background:#fff;border:3px solid var(--red)}
.badge-in{left:494px;top:1017px;width:98px;height:98px;border-radius:50%;background:var(--red);color:#fff;text-align:center}
.badge-in b{display:block;font-family:"Poppins",sans-serif;font-weight:500;font-size:36px;line-height:36px;margin-top:18px}
.badge-in span{font-size:15px}
.w-title{left:629px;top:862px;font-family:"Cinzel",serif;font-weight:700;font-size:34px;line-height:43px;color:var(--ink)}
.w-title .l2{font-weight:500}
.w-text{left:629px;top:975px;width:450px;font-size:14.5px;line-height:27.5px;color:#444}
.w-text p+p{margin-top:27px}
.btn-red{background:var(--red);color:#fff;font-family:"Cinzel",serif;font-weight:700;font-size:15px;border-radius:21px;display:flex;align-items:center;justify-content:center}

/* features */
.features{top:1370px;left:0;width:1200px;height:701px;background:var(--grey-bg)}
.card{top:167px;width:305px;height:427px;background:#fff;box-shadow:0 1px 4px rgba(0,0,0,.08)}
.card .img{height:195px}
.card h3{position:absolute;left:25px;top:210px;font-family:"Cinzel",serif;font-weight:700;font-size:18px;color:var(--ink)}
.card .addr{position:absolute;left:25px;top:241px;font-size:12.5px;line-height:19px;color:#666;width:260px}
.card .specs{position:absolute;left:25px;top:282px;width:258px;border-top:1px solid var(--line);border-bottom:1px solid var(--line);height:110px}
.spec{position:absolute;display:flex;align-items:center;gap:10px;font-size:13px;color:#333;white-space:nowrap}
.card .heart{position:absolute;left:28px;top:398px}
.card .view{position:absolute;left:167px;top:397px;color:var(--red);font-weight:700;font-size:16px}
.arrow-c{top:370px;width:30px;height:30px;border-radius:50%;border:1.5px solid #333;display:flex;align-items:center;justify-content:center}

/* why */
.why-item{top:2240px;width:190px;text-align:center;font-family:"Poppins",sans-serif;font-weight:500;font-size:15.5px;line-height:19px;color:#222}
.why-icon{width:92px;height:92px;margin:0 auto 16px;position:relative}
.why-icon .ring{position:absolute;left:-4px;top:-6px;width:90px;height:90px;border-radius:50%;border:1.5px solid #d5d5d5}
.why-icon .dot{position:absolute;left:4px;top:2px;width:86px;height:86px;border-radius:50%;display:flex;align-items:center;justify-content:center}

/* buying tips */
.tips{top:2481px;left:0;width:1200px;height:589px;background:var(--red)}
.tips-title{left:110px;top:96px;font-family:"Cinzel",serif;font-weight:700;font-size:34px;color:#fff}
.tips-list{left:110px;top:168px;width:430px;list-style:none;color:#fff;font-size:14.5px;line-height:21px}
.tips-list li{position:relative;padding-left:20px;margin-bottom:22px}
.tips-list li:before{content:"";position:absolute;left:0;top:7px;width:9px;height:9px;border-radius:50%;background:#fff}
.btn-white{left:110px;top:448px;width:128px;height:40px;border-radius:20px;background:#fff;color:var(--red);font-family:"Cinzel",serif;font-weight:700;font-size:14.5px;display:flex;align-items:center;justify-content:center}
.tips-frame{left:597px;top:97px;width:300px;height:280px;border:2px solid #fff;border-right:none;border-bottom:none}
.tips-photo{left:611px;top:112px;width:478px;height:376px;background:linear-gradient(180deg,#e4e9ef 0%,#9aa7b5 30%,#3c3a3a 55%,#d9dee4 80%,#f2f4f6 100%)}

/* contact */
.c-icon{left:138px;width:80px;height:80px;border-radius:50%;background:var(--red);display:flex;align-items:center;justify-content:center}
.c-label{left:245px;font-weight:700;font-size:14px;color:#222}
.c-val{left:245px;font-size:14px;line-height:26px;color:#222}
.field{background:#fff;box-shadow:0 2px 8px rgba(0,0,0,.12);font-size:13.5px;color:#666;padding:16px 18px}
.btn-submit{left:485px;top:3508px;width:133px;height:47px;border-radius:24px;background:var(--red);color:#fff;font-family:"Poppins",sans-serif;font-weight:600;font-size:18px;display:flex;align-items:center;justify-content:center;box-shadow:0 3px 6px rgba(0,0,0,.2)}

/* footer */
.footer-wave{left:0;top:3640px}
.footer{top:3770px;left:0;width:1200px;height:409px;background:var(--black);color:#fff;font-family:"Poppins",sans-serif}
.f-col h4{font-weight:500;font-size:21px;margin-bottom:14px;white-space:nowrap}
.f-col ul{list-style:none;font-size:15px;line-height:31px}
.f-col li{display:flex;align-items:center;gap:12px}
.f-contact{display:flex;align-items:center;gap:16px;font-size:15px;margin-bottom:28px;white-space:nowrap}
.f-contact i{width:34px;height:34px;border-radius:50%;background:var(--red);display:flex;align-items:center;justify-content:center}
.news p{font-size:14px;line-height:30px;width:300px}
.news .email{margin-top:8px;width:270px;border-bottom:1px solid #fff;padding:4px 6px 8px;font-size:14.5px}
.news .sub{margin-top:32px;margin-left:8px;width:146px;height:48px;border-radius:24px;background:var(--red);display:flex;align-items:center;justify-content:center;font-weight:600;font-size:18px}
.f-rule{left:99px;top:334px;width:1004px;height:1px;background:#555}
.copy{left:0;top:358px;width:1200px;text-align:center;font-size:15px}
</style>
</head>
<body>

<header class="abs topbar">
  <div class="abs social"><span></span><span></span><span></span><span></span></div>
  <div class="abs top-contact">
    <div><svg width="14" height="14" viewBox="0 0 24 24"><path fill="#fff" d="M6.6 10.8a15.5 15.5 0 0 0 6.6 6.6l2.2-2.2c.3-.3.7-.4 1-.2 1.1.4 2.3.6 3.6.6.6 0 1 .4 1 1V20c0 .6-.4 1-1 1A17 17 0 0 1 3 4c0-.6.4-1 1-1h3.5c.6 0 1 .4 1 1 0 1.3.2 2.5.6 3.6.1.3 0 .7-.2 1z"/></svg>+81 100 555 0142</div>
    <div><svg width="16" height="12" viewBox="0 0 16 12"><rect width="16" height="12" rx="1" fill="#fff"/><path d="M1 1l7 6 7-6" stroke="#c8282d" stroke-width="1.5" fill="none"/></svg>info@northpeakhomes.example</div>
  </div>
</header>

<nav class="abs nav">
  <div class="abs brand"><i></i>NORTHPEAK HOMES</div>
  <div class="abs menu">
    <span class="active">HOME</span><span>COMMERCIAL/INDUSTRIAL</span><span>RESIDENTIAL</span><span>BUSINESS SALES</span><span>ABOUT US</span>
  </div>
  <div class="abs btn-contact">CONTACT US</div>
</nav>

<section class="abs hero">
  <div class="hero-photo" role="img" aria-label="Modern timber and stone house at dusk with a lit pathway"></div>
  <h1 class="abs hero-title">NORTHPEAK HOMES</h1>
  <p class="abs hero-sub">An investment in Hokkaido property offers tremendous potential for both lifestyle and financial returns.</p>
  <div class="abs search">
    <div class="f" style="width:138px">Bedrooms</div>
    <div class="f" style="width:142px;padding-left:40px">Bathrooms</div>
    <div class="f" style="border:none;padding-left:28px">Property type</div>
    <div class="go">FIND PROPERTIES</div>
  </div>
  <div class="abs audience"><span class="on">RESIDENTIAL</span><span>COMMERCIAL / INDUSTRIAL</span></div>
  <svg class="abs mouse" width="24" height="48" viewBox="0 0 24 48"><rect x="2" y="1" width="20" height="30" rx="10" fill="none" stroke="#fff" stroke-width="1.5"/><line x1="12" y1="8" x2="12" y2="14" stroke="#fff" stroke-width="1.5"/><path d="M12 34v10M8 40l4 4 4-4" stroke="#fff" stroke-width="1.2" fill="none"/></svg>
  <svg class="abs hero-wave" width="1200" height="150" viewBox="0 0 1200 150">
    <path d="M380 140 C700 130 1000 100 1200 55 L1200 150 L380 150Z" fill="#c8c8c8"/>
    <path d="M340 120 C700 110 1000 70 1200 20 L1200 60 C1000 100 700 126 380 132Z" fill="#c8282d"/>
    <path d="M0 10 C120 40 260 80 420 96 C700 118 1000 80 1200 42 L1200 150 L0 150Z" fill="#fff"/>
    <path d="M400 126 C700 132 1000 100 1200 60 L1200 80 C1000 118 700 142 420 140Z" fill="#c8c8c8"/>
  </svg>
</section>

<section>
  <div class="abs w-frame"></div>
  <div class="abs w-frame-red"></div>
  <div class="abs w-frame-side"></div>
  <div class="abs w-photo" role="img" aria-label="Snowy canal town at twilight with lit warehouses"></div>
  <div class="abs badge"></div>
  <div class="abs badge-in"><b>15</b><span>Years</span></div>
  <h2 class="abs w-title">WELCOME TO<br><span class="l2">NORTHPEAK HOMES</span></h2>
  <div class="abs rule" style="left:629px;top:950px;width:62px"></div>
  <div class="abs w-text">
    <p>An investment in Hokkaido property offers tremendous potential for both lifestyle and financial returns. But, the market is complex and dynamic. To invest wisely you need advice on all the potential pitfalls.</p>
    <p>The Northpeak Homes team is small and dedicated group of professionals focused on delivering the best outcome for our clients whilst never compromising our ethical standards.</p>
  </div>
  <div class="abs btn-red" style="left:628px;top:1210px;width:129px;height:41px">READ MORE</div>
</section>

<section class="abs features">
  <h2 class="abs h2" style="top:77px">FEATURE PROPERTIES</h2>
  <div class="abs rule" style="left:576px;top:127px"></div>
  <div class="abs arrow-c" style="left:42px"><svg width="12" height="12" viewBox="0 0 12 12"><path d="M8 1L3 6l5 5" stroke="#333" stroke-width="1.5" fill="none"/></svg></div>
  <div class="abs arrow-c" style="left:1126px"><svg width="12" height="12" viewBox="0 0 12 12"><path d="M4 1l5 5-5 5" stroke="#333" stroke-width="1.5" fill="none"/></svg></div>

  <article class="abs card" style="left:110px">
    <div class="img" role="img" aria-label="Family sitting together in a bright living room" style="background:linear-gradient(180deg,#e8e2d8,#b9a48a)"></div>
    <h3>3-4 BEDROOM HOUSE</h3>
    <p class="addr">12-4 Yukimi Lane Kutchan Cho 044 000 Abuta Gun Hokkaido Japan</p>
    <div class="specs">
      <div class="spec" style="left:0;top:20px"><svg width="28" height="20" viewBox="0 0 28 20"><rect x="2" y="8" width="24" height="8" fill="none" stroke="#555" stroke-width="1.3"/><rect x="5" y="3" width="18" height="5" fill="none" stroke="#555" stroke-width="1.3"/><path d="M3 16v3M25 16v3" stroke="#555" stroke-width="1.3"/></svg>Bedrooms 7</div>
      <div class="spec" style="left:145px;top:18px"><svg width="26" height="22" viewBox="0 0 26 22"><path d="M2 11h22v4a5 5 0 0 1-5 5H7a5 5 0 0 1-5-5zM5 11V4a3 3 0 0 1 6 0" fill="none" stroke="#555" stroke-width="1.3"/></svg>Bathrooms 2</div>
      <div class="spec" style="left:0;top:62px"><svg width="28" height="24" viewBox="0 0 28 24"><path d="M2 9L14 2l12 7v13H2z" fill="none" stroke="#555" stroke-width="1.3"/><rect x="8" y="13" width="12" height="6" fill="none" stroke="#555" stroke-width="1.3"/></svg>Parking 3</div>
      <div class="spec" style="left:145px;top:62px"><svg width="26" height="24" viewBox="0 0 26 24"><path d="M2 22h22M4 22V10h5v12M10 22V3h7v19M18 22V8h5v14" fill="none" stroke="#555" stroke-width="1.3"/></svg>198.32 Sqm</div>
    </div>
    <svg class="heart" width="22" height="20" viewBox="0 0 22 20"><path d="M11 18S2 12 2 6.5A4.5 4.5 0 0 1 11 4a4.5 4.5 0 0 1 9 2.5C20 12 11 18 11 18z" fill="none" stroke="#333" stroke-width="1.4"/></svg>
    <span class="view">View Details</span>
  </article>

  <article class="abs card" style="left:447px">
    <div class="img" role="img" aria-label="Large two-storey suburban house with green lawn" style="background:linear-gradient(180deg,#d9e3ec 0%,#9aa2a8 50%,#5f8a45 100%)"></div>
    <h3>ENORMOUS HOUSE</h3>
    <p class="addr">12-4 Yukimi Lane Kutchan Cho 044 000 Abuta Gun Hokkaido Japan</p>
    <div class="specs">
      <div class="spec" style="left:0;top:20px"><svg width="28" height="20" viewBox="0 0 28 20"><rect x="2" y="8" width="24" height="8" fill="none" stroke="#555" stroke-width="1.3"/><rect x="5" y="3" width="18" height="5" fill="none" stroke="#555" stroke-width="1.3"/><path d="M3 16v3M25 16v3" stroke="#555" stroke-width="1.3"/></svg>Bedrooms 7</div>
      <div class="spec" style="left:145px;top:18px"><svg width="26" height="22" viewBox="0 0 26 22"><path d="M2 11h22v4a5 5 0 0 1-5 5H7a5 5 0 0 1-5-5zM5 11V4a3 3 0 0 1 6 0" fill="none" stroke="#555" stroke-width="1.3"/></svg>Bathrooms 2</div>
      <div class="spec" style="left:0;top:62px"><svg width="28" height="24" viewBox="0 0 28 24"><path d="M2 9L14 2l12 7v13H2z" fill="none" stroke="#555" stroke-width="1.3"/><rect x="8" y="13" width="12" height="6" fill="none" stroke="#555" stroke-width="1.3"/></svg>Parking 3</div>
      <div class="spec" style="left:145px;top:62px"><svg width="26" height="24" viewBox="0 0 26 24"><path d="M2 22h22M4 22V10h5v12M10 22V3h7v19M18 22V8h5v14" fill="none" stroke="#555" stroke-width="1.3"/></svg>198.32 Sqm</div>
    </div>
    <svg class="heart" width="22" height="20" viewBox="0 0 22 20"><path d="M11 18S2 12 2 6.5A4.5 4.5 0 0 1 11 4a4.5 4.5 0 0 1 9 2.5C20 12 11 18 11 18z" fill="none" stroke="#333" stroke-width="1.4"/></svg>
    <span class="view">View Details</span>
  </article>

  <article class="abs card" style="left:783px">
    <div class="img" role="img" aria-label="Dark modern living room with fireplace and sofa" style="background:linear-gradient(180deg,#2f3338 0%,#3d4650 60%,#8a6a55 100%)"></div>
    <h3>3-4 BEDROOM HOUSE</h3>
    <p class="addr">12-4 Yukimi Lane Kutchan Cho 044 000 Abuta Gun Hokkaido Japan</p>
    <div class="specs">
      <div class="spec" style="left:0;top:20px"><svg width="28" height="20" viewBox="0 0 28 20"><rect x="2" y="8" width="24" height="8" fill="none" stroke="#555" stroke-width="1.3"/><rect x="5" y="3" width="18" height="5" fill="none" stroke="#555" stroke-width="1.3"/><path d="M3 16v3M25 16v3" stroke="#555" stroke-width="1.3"/></svg>Bedrooms 7</div>
      <div class="spec" style="left:145px;top:18px"><svg width="26" height="22" viewBox="0 0 26 22"><path d="M2 11h22v4a5 5 0 0 1-5 5H7a5 5 0 0 1-5-5zM5 11V4a3 3 0 0 1 6 0" fill="none" stroke="#555" stroke-width="1.3"/></svg>Bathrooms 2</div>
      <div class="spec" style="left:0;top:62px"><svg width="28" height="24" viewBox="0 0 28 24"><path d="M2 9L14 2l12 7v13H2z" fill="none" stroke="#555" stroke-width="1.3"/><rect x="8" y="13" width="12" height="6" fill="none" stroke="#555" stroke-width="1.3"/></svg>Parking 3</div>
      <div class="spec" style="left:145px;top:62px"><svg width="26" height="24" viewBox="0 0 26 24"><path d="M2 22h22M4 22V10h5v12M10 22V3h7v19M18 22V8h5v14" fill="none" stroke="#555" stroke-width="1.3"/></svg>198.32 Sqm</div>
    </div>
    <svg class="heart" width="22" height="20" viewBox="0 0 22 20"><path d="M11 18S2 12 2 6.5A4.5 4.5 0 0 1 11 4a4.5 4.5 0 0 1 9 2.5C20 12 11 18 11 18z" fill="none" stroke="#333" stroke-width="1.4"/></svg>
    <span class="view">View Details</span>
  </article>
</section>

<section>
  <h2 class="abs h2" style="top:2145px">Why Hokkaido?</h2>
  <div class="abs rule" style="left:570px;top:2193px;width:62px"></div>
  <div class="abs why-item" style="left:156px">
    <div class="why-icon"><div class="ring"></div><div class="dot" style="background:var(--red)"><svg width="40" height="40" viewBox="0 0 40 40" fill="none" stroke="#fff" stroke-width="2"><circle cx="20" cy="20" r="14"/><path d="M6 20h28M20 6c6 6 6 22 0 28M20 6c-6 6-6 22 0 28"/></svg></div></div>
    15+ years of rising<br>tourism
  </div>
  <div class="abs why-item" style="left:394px">
    <div class="why-icon"><div class="ring"></div><div class="dot" style="background:#222"><svg width="40" height="40" viewBox="0 0 40 40" stroke="#fff" stroke-width="2"><path d="M20 4v32M6 12l28 16M34 12L6 28"/></svg></div></div>
    Highest snowfall<br>in the world
  </div>
  <div class="abs why-item" style="left:633px">
    <div class="why-icon"><div class="ring"></div><div class="dot" style="background:var(--red)"><svg width="40" height="40" viewBox="0 0 40 40" fill="none" stroke="#fff" stroke-width="2"><path d="M10 20l10-10 10 10v12H10z"/><path d="M4 30l8 6h16l8-6"/></svg></div></div>
    Foreign ownership<br>allowed
  </div>
  <div class="abs why-item" style="left:872px">
    <div class="why-icon"><div class="ring"></div><div class="dot" style="background:#222"><svg width="40" height="40" viewBox="0 0 40 40" fill="none" stroke="#fff" stroke-width="2"><path d="M6 34h28M10 34V14l8-6v26M22 34V20h10v14M25 14l5-5 3 3"/></svg></div></div>
    Strong rental<br>yields
  </div>
</section>

<section class="abs tips">
  <h2 class="abs tips-title">Buying Tips</h2>
  <div class="abs" style="left:110px;top:140px;width:58px;height:3px;background:#fff"></div>
  <ul class="abs tips-list">
    <li>Is the land freehold (not all land in Niseko is freehold)?</li>
    <li>What is the zoning of the land, and what implications does that have?</li>
    <li>What are the building code guidelines for this area and this zoning?</li>
    <li>Who is the vendor?<br>How long has the vendor owned the property?</li>
    <li>Why is the vendor selling?</li>
  </ul>
  <div class="abs btn-white">READ MORE</div>
  <div class="abs tips-frame"></div>
  <div class="abs tips-photo" role="img" aria-label="Snow-covered wooden cabin in deep winter snow"></div>
</section>

<section>
  <h2 class="abs h2" style="top:3167px">Contact Us</h2>
  <div class="abs rule" style="left:566px;top:3214px;width:68px"></div>

  <div class="abs c-icon" style="top:3250px"><svg width="34" height="26" viewBox="0 0 34 26"><rect width="34" height="26" rx="3" fill="#fff"/><path d="M2 3l15 12L32 3" stroke="#c8282d" stroke-width="3" fill="none"/></svg></div>
  <div class="abs c-label" style="top:3265px">EMAIL:</div>
  <div class="abs c-val" style="top:3288px">info@northpeakhomes.example</div>

  <div class="abs c-icon" style="top:3354px"><svg width="34" height="34" viewBox="0 0 24 24"><path fill="#fff" d="M6.6 10.8a15.5 15.5 0 0 0 6.6 6.6l2.2-2.2c.3-.3.7-.4 1-.2 1.1.4 2.3.6 3.6.6.6 0 1 .4 1 1V20c0 .6-.4 1-1 1A17 17 0 0 1 3 4c0-.6.4-1 1-1h3.5c.6 0 1 .4 1 1 0 1.3.2 2.5.6 3.6.1.3 0 .7-.2 1z"/></svg></div>
  <div class="abs c-label" style="top:3370px">PHONE:</div>
  <div class="abs c-val" style="top:3393px;left:248px">+81 100 555 0142</div>

  <div class="abs c-icon" style="top:3456px"><svg width="30" height="36" viewBox="0 0 30 36"><path d="M15 2a10 10 0 0 0-10 10c0 8 10 18 10 18s10-10 10-18A10 10 0 0 0 15 2z" fill="none" stroke="#fff" stroke-width="2.5"/><circle cx="15" cy="12" r="3.5" fill="#fff"/><ellipse cx="15" cy="32" rx="11" ry="3" fill="none" stroke="#fff" stroke-width="2"/></svg></div>
  <div class="abs c-label" style="top:3468px">ADDRESS:</div>
  <div class="abs c-val" style="top:3491px">1180 Cedar Ridge Ave. #204<br>Lakeview, CA 90000</div>

  <div class="abs field" style="left:485px;top:3250px;width:282px;height:48px">First Name</div>
  <div class="abs field" style="left:778px;top:3250px;width:284px;height:48px">Last Name</div>
  <div class="abs field" style="left:485px;top:3313px;width:282px;height:49px">Phone Number</div>
  <div class="abs field" style="left:778px;top:3313px;width:284px;height:49px">Email</div>
  <div class="abs field" style="left:485px;top:3376px;width:577px;height:110px">Message</div>
  <div class="abs btn-submit">Submit</div>
</section>

<svg class="abs footer-wave" width="1200" height="140" viewBox="0 0 1200 140">
  <path d="M0 60 C150 30 400 20 700 26 C900 30 1050 50 1200 80 L1200 140 L0 140Z" fill="#cfcfcf"/>
  <path d="M0 78 C150 48 400 38 700 40 C900 44 1050 70 1200 96 L1200 140 L0 140Z" fill="#c8282d"/>
  <path d="M0 100 C200 70 450 58 700 60 C900 64 1050 90 1200 112 L1200 140 L0 140Z" fill="#000"/>
</svg>
<footer class="abs footer">
  <div class="abs f-col" style="left:110px;top:36px">
    <h4>Quick Links</h4>
    <ul>
      <li><svg width="14" height="12" viewBox="0 0 14 12"><path d="M1 6h11M7 1l5 5-5 5" stroke="#fff" stroke-width="2" fill="none"/></svg>Home</li>
      <li><svg width="14" height="12" viewBox="0 0 14 12"><path d="M1 6h11M7 1l5 5-5 5" stroke="#fff" stroke-width="2" fill="none"/></svg>About Us</li>
      <li><svg width="14" height="12" viewBox="0 0 14 12"><path d="M1 6h11M7 1l5 5-5 5" stroke="#fff" stroke-width="2" fill="none"/></svg>For Sale</li>
      <li><svg width="14" height="12" viewBox="0 0 14 12"><path d="M1 6h11M7 1l5 5-5 5" stroke="#fff" stroke-width="2" fill="none"/></svg>Property Alert</li>
      <li><svg width="14" height="12" viewBox="0 0 14 12"><path d="M1 6h11M7 1l5 5-5 5" stroke="#fff" stroke-width="2" fill="none"/></svg>Buying Tips</li>
      <li><svg width="14" height="12" viewBox="0 0 14 12"><path d="M1 6h11M7 1l5 5-5 5" stroke="#fff" stroke-width="2" fill="none"/></svg>Selling</li>
    </ul>
  </div>
  <div class="abs f-col" style="left:297px;top:36px">
    <h4>Other Links</h4>
    <ul>
      <li><svg width="14" height="12" viewBox="0 0 14 12"><path d="M1 6h11M7 1l5 5-5 5" stroke="#fff" stroke-width="2" fill="none"/></svg>FAQ</li>
      <li><svg width="14" height="12" viewBox="0 0 14 12"><path d="M1 6h11M7 1l5 5-5 5" stroke="#fff" stroke-width="2" fill="none"/></svg>Tems of Use</li>
      <li><svg width="14" height="12" viewBox="0 0 14 12"><path d="M1 6h11M7 1l5 5-5 5" stroke="#fff" stroke-width="2" fill="none"/></svg>Privacy Policy</li>
      <li><svg width="14" height="12" viewBox="0 0 14 12"><path d="M1 6h11M7 1l5 5-5 5" stroke="#fff" stroke-width="2" fill="none"/></svg>Support Links</li>
      <li><svg width="14" height="12" viewBox="0 0 14 12"><path d="M1 6h11M7 1l5 5-5 5" stroke="#fff" stroke-width="2" fill="none"/></svg>Conditions</li>
    </ul>
  </div>
  <div class="abs f-col" style="left:501px;top:36px">
    <h4 style="margin-bottom:20px">Contact Us</h4>
    <div class="f-contact"><i><svg width="12" height="16" viewBox="0 0 12 16"><path d="M6 1a5 5 0 0 0-5 5c0 4 5 9 5 9s5-5 5-9a5 5 0 0 0-5-5z" fill="#fff"/><circle cx="6" cy="6" r="2" fill="#c8282d"/></svg></i>Company Name,United State.</div>
    <div class="f-contact"><i><svg width="14" height="10" viewBox="0 0 14 10"><rect width="14" height="10" rx="1" fill="#fff"/><path d="M1 1l6 5 6-5" stroke="#c8282d" stroke-width="1.4" fill="none"/></svg></i>info@northpeakhomes.example</div>
    <div class="f-contact"><i><svg width="14" height="14" viewBox="0 0 24 24"><path fill="#fff" d="M6.6 10.8a15.5 15.5 0 0 0 6.6 6.6l2.2-2.2c.3-.3.7-.4 1-.2 1.1.4 2.3.6 3.6.6.6 0 1 .4 1 1V20c0 .6-.4 1-1 1A17 17 0 0 1 3 4c0-.6.4-1 1-1h3.5c.6 0 1 .4 1 1 0 1.3.2 2.5.6 3.6.1.3 0 .7-.2 1z"/></svg></i>+1 555 010 2200</div>
  </div>
  <div class="abs f-col news" style="left:811px;top:36px">
    <h4 style="margin-bottom:10px">Sign Up Our Newsletter</h4>
    <p>Lorem ipsum dolor sit amet,consectetur adipiscing elit,adipiscing elit.</p>
    <div class="email">Email</div>
    <div class="sub">Subscribe</div>
  </div>
  <div class="abs f-rule"></div>
  <div class="abs copy">Copyrights@2026.Company Name.All Rights Reserved</div>
</footer>

</body>
</html>
```